Website Design for Camp 3874

We need a website design for a new company that strives to provide training and structure for religious missionaries who are traveling the world to teach of christianity.
They provide training in:
- Nutrition Coaching & Daily assignments
- Personal Training Sessions
- Phycological emotional/mental component
The goal of Camp 3874 is to help missionaries preach the gospel of christ to those who haven't heard it due to geographical obstacles and physical limitations that get in the way.
The homepage template has linked images to use. If any other images are needed, stock images are acceptable.

Logo/Color Scheme: https://files.nervalo.example/folders/8Kp2QwZr7LmXv4TsN9bHc3YdJ6fGaE1Ru?share=open

Customer Avatar/Core Message Canvas: https://sheets.nervalo.example/s/d/7Hq39TbWmuKpZr2LxNcV8yEs5DfGa4JkQo1BnXtYRMwP/edit?share=open

Homepage Template: https://pages.nervalo.example/doc/d/5nRZ82kLp94QsWxTy7mBuVhCe3DjFa6Go0PiKqNr4Ytw/edit?share=open

```html
<!DOCTYPE html>
<html lang="en">
<head>
<meta charset="utf-8">
<title>Camp 3874 — Missionary Training</title>
<link rel="stylesheet" href="https://fonts.googleapis.com/css2?family=Montserrat:wght@400;500;600;700;800&display=swap">
<style>
:root{
  --forest:#2b3a18;
  --forest-deep:#233014;
  --olive:#5d6d36;
  --olive-text:#5f6f34;
  --gold:#e2bd3f;
  --gold-soft:#f3e4ad;
  --ink:#141414;
  --muted:#3a3a3a;
  --white:#ffffff;
  --line:#c9c9c9;
}
*{margin:0;padding:0;box-sizing:border-box}
html,body{width:1200px;height:4860px;overflow:hidden}
body{position:relative;background:var(--white);font-family:"Montserrat",sans-serif;color:var(--ink)}
.abs{position:absolute}
.center{left:0;width:1200px;text-align:center}
.eyebrow{font-size:16px;font-weight:600;letter-spacing:.3px}
.section-title{font-size:34px;font-weight:700;line-height:1.1;text-transform:uppercase}
.body-copy{font-size:12.5px;line-height:24px;color:var(--muted)}
.btn{position:absolute;display:flex;align-items:center;justify-content:center;font-size:12px;font-weight:700;text-transform:uppercase;letter-spacing:.3px;border-radius:4px}

/* Hero */
.hero-photo{left:0;top:0;width:1200px;height:835px;
  background:linear-gradient(90deg,rgba(255,255,255,.95) 0%,rgba(255,255,255,.7) 25%,rgba(255,255,255,0) 55%),
  linear-gradient(180deg,#b9c6d4 0%,#8d9aa6 25%,#6f7560 55%,#5b5a45 80%,#8a8270 100%)}
.hero-cut{left:0;top:790px;width:1200px;height:50px}
.brand{font-weight:800;color:var(--forest);letter-spacing:1px}
.nav a{position:absolute;top:108px;font-size:12px;font-weight:500;color:var(--ink);text-decoration:none;text-transform:uppercase}
.signup{left:908px;top:95px;width:167px;height:41px;background:var(--forest);color:var(--white)}
.hero-rail{left:63px;top:120px;width:1px;height:640px;background:#8e8e8e}
.mouse{left:55px;top:428px;width:16px;height:24px;border:1.5px solid #6a6a6a;border-radius:8px;background:var(--white)}
.mouse::after{content:"";position:absolute;left:6px;top:4px;width:2px;height:6px;background:#6a6a6a;border-radius:1px}
.hero-kicker{left:125px;top:274px;font-size:20px;font-weight:700;color:var(--forest)}
.hero-title{left:125px;top:308px;font-size:42px;font-weight:800;line-height:43px;color:var(--ink);text-transform:uppercase}
.hero-copy{left:125px;top:465px;font-size:13px;font-weight:500;line-height:25px}
.btn-outline-dark{left:125px;top:558px;width:258px;height:40px;border:1.5px solid var(--forest);color:var(--forest)}
.btn-gold{left:403px;top:558px;width:259px;height:40px;background:var(--gold);color:var(--forest)}

/* Staff */
.staff-photo{position:absolute;border-radius:2px}
.arrow{position:absolute;width:40px;height:40px;border-radius:50%}

/* Dark band */
.band{left:0;width:1200px}
.on-dark{color:var(--white)}
.on-dark .body-copy,.on-dark.body-copy{color:#eef0e6}
.btn-outline-light{border:1.5px solid var(--white);color:var(--white)}

/* Approach */
.tab{position:absolute;top:2248px;font-size:24px;font-weight:700}
.tab-sep{position:absolute;top:2256px;width:1px;height:14px;background:#9a9a9a}
.btn-dark{background:var(--forest);color:var(--white)}

/* Who */
.who-icon{position:absolute;width:74px;height:74px;border-radius:50%;background:var(--white);display:flex;align-items:center;justify-content:center}
.who-title{position:absolute;font-size:16px;font-weight:600;color:var(--white);text-transform:uppercase}
.who-copy{position:absolute;font-size:9.5px;line-height:19px;color:#eef0e3}

/* Footer */
.foot-link{position:absolute;left:553px;width:130px;margin-left:-65px;text-align:center;font-size:13px;color:var(--white)}
.contact-dot{position:absolute;left:806px;width:34px;height:34px;border-radius:50%;background:var(--gold);display:flex;align-items:center;justify-content:center}
.contact-text{position:absolute;left:855px;font-size:13px;line-height:24px;color:var(--white)}
.social{position:absolute;top:4670px;width:22px;height:22px;border-radius:50%;background:var(--gold)}
</style>
</head>
<body>

<!-- Hero -->
<div class="abs hero-photo" role="img" aria-label="Hiker with a red jacket and backpack standing on a rocky mountain trail above a wide alpine valley"></div>
<svg class="abs hero-cut" viewBox="0 0 1200 50" preserveAspectRatio="none"><polygon points="1200,0 1200,50 0,50 0,45 1070,45" fill="#ffffff"/></svg>

<div class="abs center brand" style="top:8px;font-size:44px;line-height:56px">CAMP 3874</div>
<nav class="nav">
  <a style="left:125px">Programs</a>
  <a style="left:280px">Events</a>
  <a style="left:410px">Online Store</a>
  <a style="left:587px">About Us</a>
  <a style="left:733px">Contact Us</a>
</nav>
<div class="btn signup">Sign Up</div>

<div class="abs hero-rail"></div>
<div class="abs mouse"></div>

<div class="abs hero-kicker">EMPOWING CHANGE:</div>
<h1 class="abs hero-title">By illuminating lives<br>unexposed to the<br>gospel’s light</h1>
<p class="abs hero-copy">Camp 3874’s mission is to enable the word of Jesus to be experienced<br>by people in the most remote and treacherous parts of the world</p>
<div class="btn btn-outline-dark">View Our Programs</div>
<div class="btn btn-gold">Resgister For Training</div>

<!-- Staff -->
<div class="abs center eyebrow" style="top:932px">CAMP 3874’S</div>
<h2 class="abs center section-title" style="top:966px">Well-rounded staff for<br>specialized training</h2>
<p class="abs center body-copy" style="top:1064px">Lorem Ipsum is simply dummy text of the printing and typesetting industry. Lorem Ipsum has been the industry’s<br>standard dummy text ever since the 1500s, when an unknown printer took.</p>

<div class="arrow" style="left:42px;top:1243px;background:var(--gold-soft)"><svg width="40" height="40" viewBox="0 0 40 40"><path d="M27 20H13M18 14l-6 6 6 6" stroke="#2b3a18" stroke-width="3" fill="none" stroke-linecap="round" stroke-linejoin="round"/></svg></div>
<div class="staff-photo" style="left:100px;top:1190px;width:168px;height:145px;background:linear-gradient(160deg,#e9e6e1,#b89a80)" role="img" aria-label="Staff member reading a tablet"></div>
<div class="staff-photo" style="left:285px;top:1183px;width:168px;height:144px;background:linear-gradient(160deg,#9fb0bf,#3d4650)" role="img" aria-label="Trainer crouching on stairs during a workout"></div>
<div class="staff-photo" style="left:470px;top:1150px;width:260px;height:192px;background:linear-gradient(160deg,#eceae6,#8f7a66 70%,#5a4a3c)" role="img" aria-label="Nutrition coach preparing a meal in a kitchen"></div>
<div class="staff-photo" style="left:748px;top:1183px;width:168px;height:144px;background:linear-gradient(160deg,#f1ece4,#b5462e 60%,#5e7c34)" role="img" aria-label="Fresh vegetables and a jar of prepared food"></div>
<div class="staff-photo" style="left:932px;top:1190px;width:168px;height:145px;background:linear-gradient(160deg,#2b2e33,#0d0f12)" role="img" aria-label="Field instructor in dark tactical gear"></div>
<div class="arrow" style="left:1118px;top:1243px;background:var(--olive)"><svg width="40" height="40" viewBox="0 0 40 40"><path d="M13 20h14M22 14l6 6-6 6" stroke="#fff" stroke-width="3" fill="none" stroke-linecap="round" stroke-linejoin="round"/></svg></div>

<!-- Breaking barriers -->
<svg class="abs band" style="top:1410px;height:612px" viewBox="0 0 1200 612" preserveAspectRatio="none"><polygon points="0,0 130,33 1200,33 1200,560 1070,612 0,612" fill="#2b3a18"/></svg>
<div class="abs center eyebrow on-dark" style="top:1542px">CAMP 3874’S</div>
<h2 class="abs center section-title on-dark" style="top:1575px">Why its breaking barriers</h2>
<div class="abs center on-dark body-copy" style="top:1636px">
  <p>Geographical challenges make some communities difficult for missionaries to reach. The Camp 3874 program is designed to remove<br>the physical limitations that can hinder us from bringing the Gospel to places that seem physically impossible to reach. Camp 3874 is<br>founded on Romans 15:20. In his letter to the Romans, Paul requests funding to take the Gospel to Spain. In this letter, he writes:</p>
  <p style="margin-top:24px">“[20] and thus I make it my ambition to preach the gospel, not where Christ has already been named, lest I build on someone else’s<br>foundation, [21] but it is written, “those who have never been told of him will see, and those who have never heard will understand</p>
  <p style="margin-top:18px">(Romans 15:20-21)</p>
</div>
<div class="btn btn-outline-light" style="left:470px;top:1879px;width:260px;height:40px">Join Our Mission</div>

<!-- Approach -->
<div class="abs center eyebrow" style="top:2118px">CAMP 3874’S</div>
<h2 class="abs center section-title" style="top:2150px">Missionary training approach</h2>
<div class="tab" style="left:199px;color:var(--olive-text)">MIND</div>
<div class="tab-sep" style="left:413px"></div>
<div class="tab" style="left:556px">BODY</div>
<div class="tab-sep" style="left:775px"></div>
<div class="tab" style="left:916px">SPIRIT</div>
<div class="abs" style="left:205px;top:2347px;width:790px;height:305px;background:linear-gradient(180deg,#c9d6dc 0%,#8e9a8a 35%,#5b4a2e 65%,#3e4a3a 85%,#8b8f8f 100%)" role="img" aria-label="Forest river valley at sunset with granite cliffs"></div>
<p class="abs center body-copy" style="top:2697px">Psychologically, we will prepare the mind through counseling, breathing techniques, and simulations in order to<br>prepare for psychological challenges that come with being in the field.</p>
<div class="btn btn-dark" style="left:408px;top:2788px;width:384px;height:40px">View Our Detailed Training Program</div>

<!-- Who is it for -->
<svg class="abs band" style="top:2875px;height:940px" viewBox="0 0 1200 940" preserveAspectRatio="none"><polygon points="0,0 130,55 1200,55 1200,885 1070,940 0,940" fill="#5d6d36"/></svg>
<div class="abs center eyebrow on-dark" style="top:3028px">CAMP 3874’S</div>
<h2 class="abs center section-title on-dark" style="top:3061px">Who is Camp 3874 for?</h2>
<div class="abs" style="left:600px;top:3150px;width:1px;height:470px;background:#c9d0b4"></div>
<div class="abs" style="left:562px;top:3222px;width:38px;height:1px;background:#c9d0b4"></div>
<div class="abs" style="left:600px;top:3368px;width:38px;height:1px;background:#c9d0b4"></div>
<div class="abs" style="left:562px;top:3525px;width:38px;height:1px;background:#c9d0b4"></div>

<div class="who-icon" style="left:488px;top:3185px"><svg width="36" height="36" viewBox="0 0 36 36"><rect x="4" y="11" width="28" height="20" rx="2" fill="#e2bd3f"/><path d="M13 11V7h10v4" stroke="#e2bd3f" stroke-width="2.5" fill="none"/><rect x="4" y="18" width="28" height="2" fill="#fff"/></svg></div>
<div class="who-title" style="left:625px;top:3160px">Sending agencies for missionaries</div>
<p class="who-copy" style="left:625px;top:3193px;width:445px">Are you looking to improve the training you’re offering your flock? We have designed a program to align our training with your goals to spread the Gospel to people and places where Jesus remains unnamed &amp; unknown. Our training helps turn your missionaries to resilient, well-trained men and women</p>

<div class="who-title" style="left:125px;top:3312px;width:450px;text-align:right">Missionaries</div>
<p class="who-copy" style="left:125px;top:3345px;width:450px;text-align:right">Are you independently seeking to develop your knowledge and skills independently? We are here to help! We can customize a training approach that fits your specific needs. Let us support your missionary journey to spread the Gospel to the most remote and treacherous areas in the world.</p>
<div class="who-icon" style="left:638px;top:3331px"><svg width="36" height="36" viewBox="0 0 36 36"><circle cx="17" cy="19" r="12" fill="none" stroke="#e2bd3f" stroke-width="3"/><circle cx="17" cy="19" r="6" fill="none" stroke="#e2bd3f" stroke-width="3"/><circle cx="17" cy="19" r="2" fill="#e2bd3f"/><path d="M18 18L30 6M26 5h5v5" stroke="#e2bd3f" stroke-width="2.5" fill="none"/></svg></div>

<div class="who-icon" style="left:488px;top:3488px"><svg width="36" height="36" viewBox="0 0 36 36"><rect x="7" y="9" width="22" height="15" rx="1.5" fill="none" stroke="#e2bd3f" stroke-width="3"/><rect x="3" y="26" width="30" height="4" rx="1" fill="#e2bd3f"/><path d="M14 4l4-2 4 2-4 2z" fill="#e2bd3f"/></svg></div>
<div class="who-title" style="left:625px;top:3465px">Christian-based training program for all!</div>
<p class="who-copy" style="left:625px;top:3498px;width:445px">Are you looking to improve the training you’re offering your flock? We have designed a program to align our training with your goals to spread the Gospel to people and places where Jesus remains unnamed &amp; unknown. Our training helps turn your missionaries to resilient, well-trained men and women</p>

<div class="btn btn-outline-light" style="left:430px;top:3668px;width:340px;height:40px">View Our Training Options</div>

<!-- Newsletter -->
<div class="abs center eyebrow" style="top:3908px">CAMP 3874’S</div>
<h2 class="abs center section-title" style="top:3942px">Join our missionary training:</h2>
<p class="abs center" style="top:4004px;font-size:14px;font-weight:600;line-height:24px">Join our Missionary Training: Stay up-to-date on our training programs, missionary success stories, and<br>new program info</p>
<div class="abs" style="left:268px;top:4098px;width:664px;height:47px;border:1.5px solid #b9bfa8"></div>
<div class="abs" style="left:310px;top:4115px;font-size:12px;font-weight:600;color:#8b8b8b">EMAIL NOW</div>
<div class="btn btn-dark" style="left:715px;top:4102px;width:210px;height:39px">Submit Now</div>

<!-- Footer -->
<svg class="abs band" style="top:4215px;height:645px" viewBox="0 0 1200 645" preserveAspectRatio="none"><polygon points="0,0 130,30 1200,30 1200,645 0,645" fill="#2b3a18"/></svg>
<div class="abs" style="left:493px;top:4340px;width:214px;height:82px;background:var(--white);display:flex;align-items:center;justify-content:center"><span class="brand" style="font-size:32px">CAMP 3874</span></div>
<p class="abs" style="left:125px;top:4482px;width:300px;font-size:13px;line-height:25px;color:var(--white)">Lorem Ipsum is simply dummy text of the printing and typesetting industry. Lorem Ipsum has been the industry’s standard dummy text ever since the 1500s, when an unknown printer took a galley of type and scrambled it to make a type specimen book.</p>
<div class="social" style="left:126px"></div>
<div class="social" style="left:168px"></div>
<div class="social" style="left:210px"></div>

<div class="abs" style="left:488px;top:4466px;width:130px;text-align:center;font-size:20px;font-weight:600;color:var(--white)">Quick Links</div>
<div class="abs" style="left:492px;top:4510px;width:1px;height:180px;background:#8d9878"></div>
<div class="abs" style="left:748px;top:4510px;width:1px;height:180px;background:#8d9878"></div>
<div class="foot-link" style="top:4520px">Programs</div>
<div class="foot-link" style="top:4555px">Events</div>
<div class="foot-link" style="top:4590px">Online Stores</div>
<div class="foot-link" style="top:4625px">About Us</div>
<div class="foot-link" style="top:4660px">Case Studies</div>

<div class="abs" style="left:806px;top:4466px;font-size:20px;font-weight:600;color:var(--white)">Contact info</div>
<div class="contact-dot" style="top:4518px"><svg width="16" height="16" viewBox="0 0 16 16"><path d="M4 2l2 3-1.5 1.5c.8 1.8 2.2 3.2 4 4L10 9l3 2-1 3C7 14 2 9 2 4z" fill="#2b3a18"/></svg></div>
<div class="contact-text" style="top:4523px">+1 (555) 014-2290</div>
<div class="contact-dot" style="top:4584px"><svg width="16" height="16" viewBox="0 0 16 16"><rect x="2" y="4" width="12" height="9" rx="1" fill="#2b3a18"/><path d="M2 5l6 4 6-4" stroke="#e2bd3f" stroke-width="1.3" fill="none"/></svg></div>
<div class="contact-text" style="top:4589px">lorem@ipsum.com</div>
<div class="contact-dot" style="top:4652px"><svg width="16" height="16" viewBox="0 0 16 16"><path d="M8 15s5-5 5-9a5 5 0 00-10 0c0 4 5 9 5 9z" fill="#2b3a18"/><circle cx="8" cy="6" r="1.8" fill="#e2bd3f"/></svg></div>
<div class="contact-text" style="top:4645px">Lorem Ipsum is simply dummy<br>text of the printing</div>

<div class="abs" style="left:0;top:4820px;width:1200px;height:40px;background:var(--forest-deep)"></div>
<div class="abs center" style="top:4832px;font-size:12px;color:#dfe3d4">Copyright © 2023 <b style="color:#fff">Camp 3874</b>. All Rights Reserved. Terms And Condition</div>

</body>
</html>
```